Bref créative
Stationary and Business cards for Criminal Defense Firm
Daniel R. Halvorsen - Attorney at Law
Professional
Daniel R Halvorsen
418 N. 7th Street
Columbus, OH 43207
Daniel@verdictwithhalvorsen.example
VerdictWithHalvorsen.example

```html
<!DOCTYPE html>
<html lang="en">
<head>
<meta charset="utf-8">
<title>Daniel R. Halvorsen – Attorney at Law · Stationery Set</title>
<link href="https://fonts.googleapis.com/css2?family=Lato:wght@400;700&display=swap" rel="stylesheet">
<style>
  :root{
    --bg:#e4e5e7;
    --paper:#fbfbfb;
    --navy:#3b3a5c;
    --ink:#55585e;
    --muted:#9a9da3;
    --rule:#d3d5d8;
    --pocket:#eeeff1;
    --band:#c9cbcf;
    --card-dark:#5b5d62;
    --shadow:0 2px 6px rgba(0,0,0,.12);
  }
  *{box-sizing:border-box;margin:0;padding:0}
  html,body{width:1200px;height:482px;overflow:hidden;background:var(--bg)}
  body{font-family:"Lato",Arial,sans-serif;color:var(--ink)}
  .canvas{position:relative;width:1200px;height:482px}
  .sheet{position:absolute;background:var(--paper);box-shadow:var(--shadow)}

  /* brand lockup */
  .brand{display:flex;align-items:center;gap:4px;color:var(--navy)}
  .brand-square{width:12px;height:12px;background:var(--navy);flex:none}
  .brand-name{font-weight:700;font-size:6.5px;letter-spacing:.08em;text-transform:uppercase;line-height:1}
  .brand.light{color:#fff}
  .brand.light .brand-square{background:#fff}

  /* letterhead */
  .letterhead{left:24px;top:22px;width:226px;height:320px;padding:18px 18px 14px}
  .letterhead .date{margin-top:26px;font-size:4.5px}
  .letter-body{margin-top:10px;font-size:4.5px;line-height:1.7}
  .letter-body p{margin-bottom:5px}
  .signature{width:70px;height:16px;margin-top:6px;background:linear-gradient(90deg,#e6e7ea,#f4f4f5)}
  .letter-sign{font-size:4.5px;margin-top:3px}
  .letter-footer{position:absolute;left:18px;right:18px;bottom:14px;border-top:.5px solid var(--rule);padding-top:5px;display:flex;justify-content:space-between;font-size:4px;color:var(--muted)}

  /* envelopes */
  .envelope{left:264px;width:240px}
  .envelope-front{top:22px;height:108px;padding:12px}
  .return-address{margin-top:5px;font-size:4px;line-height:1.5;color:var(--muted)}
  .envelope-back{top:150px;height:118px}
  .envelope-back svg{position:absolute;inset:0}

  /* business cards */
  .card{top:362px;width:150px;height:86px;padding:11px}
  .card-front{left:24px}
  .card-back{left:184px;background:var(--card-dark);display:flex;align-items:center;justify-content:center}
  .card-name{margin-top:12px;font-size:6px;font-weight:700;color:var(--navy)}
  .card-role{font-size:4.5px;color:var(--muted);margin-bottom:6px}
  .card-contact{font-size:4px;line-height:1.55}

  /* presentation folders */
  .folder{position:absolute;background:var(--paper);box-shadow:var(--shadow);overflow:hidden}
  .folder-open{left:670px;top:16px;width:400px;height:256px;display:flex}
  .folder-panel{position:relative;flex:1}
  .folder-panel+.folder-panel{border-left:.5px solid var(--rule)}
  .pocket{position:absolute;left:0;right:0;bottom:0;height:40%;background:var(--pocket);border-top:.5px solid var(--rule)}
  .pocket-band{position:absolute;left:0;right:0;top:12px;height:14px;background:linear-gradient(180deg,var(--band),var(--pocket))}
  .pocket-content{position:absolute;left:14px;right:14px;top:34px;display:flex;align-items:center;justify-content:space-between}
  .folder-web{font-size:5px;color:var(--muted)}
  .folder-closed{top:290px;width:152px;height:182px}
  .folder-front{left:704px}
  .folder-rear{left:884px}
  .folder-closed .pocket-content{left:10px;right:10px}
</style>
</head>
<body>
<main class="canvas">

  <article class="sheet letterhead">
    <div class="brand"><span class="brand-square"></span><span class="brand-name">Daniel R. Halvorsen</span></div>
    <p class="date">March 4, 2024</p>
    <div class="letter-body">
      <p>Dear Client,</p>
      <p>Thank you for choosing our firm to represent you.</p>
      <p>We review every detail of your case with care and will respond promptly to any question you may have.</p>
      <p>Please call our office to schedule your next meeting.</p>
      <p>Sincerely,</p>
    </div>
    <div class="signature" role="img" aria-label="Handwritten signature"></div>
    <p class="letter-sign">Daniel R Halvorsen</p>
    <footer class="letter-footer">
      <span>418 N. 7th Street, Columbus, OH 43207</span>
      <span>VerdictWithHalvorsen.example</span>
    </footer>
  </article>

  <section class="sheet envelope envelope-front">
    <div class="brand"><span class="brand-square"></span><span class="brand-name">Daniel R. Halvorsen</span></div>
    <p class="return-address">418 N. 7th Street<br>Columbus, OH 43207</p>
  </section>

  <section class="sheet envelope envelope-back">
    <svg width="240" height="118" viewBox="0 0 240 118" aria-hidden="true">
      <polyline points="0,0 120,62 240,0" fill="none" stroke="#d3d5d8" stroke-width=".8"/>
      <line x1="0" y1="118" x2="96" y2="52" stroke="#e0e1e4" stroke-width=".6"/>
      <line x1="240" y1="118" x2="144" y2="52" stroke="#e0e1e4" stroke-width=".6"/>
    </svg>
  </section>

  <section class="sheet card card-front">
    <div class="brand"><span class="brand-square"></span><span class="brand-name">Daniel R. Halvorsen</span></div>
    <p class="card-name">Daniel R Halvorsen</p>
    <p class="card-role">Attorney at Law</p>
    <div class="card-contact">
      <p>614.555.0142</p>
      <p>Daniel@verdictwithhalvorsen.example</p>
      <p>418 N. 7th Street, Columbus, OH 43207</p>
    </div>
  </section>

  <section class="sheet card card-back">
    <div class="brand light"><span class="brand-square"></span><span class="brand-name">Daniel R. Halvorsen</span></div>
  </section>

  <section class="folder folder-open">
    <div class="folder-panel">
      <div class="pocket">
        <div class="pocket-band"></div>
        <div class="pocket-content"><span class="folder-web">VerdictWithHalvorsen.example</span></div>
      </div>
    </div>
    <div class="folder-panel">
      <div class="pocket">
        <div class="pocket-band"></div>
        <div class="pocket-content"><span></span><div class="brand"><span class="brand-square"></span><span class="brand-name">Daniel R. Halvorsen</span></div></div>
      </div>
    </div>
  </section>

  <section class="folder folder-closed folder-front">
    <div class="pocket">
      <div class="pocket-band"></div>
      <div class="pocket-content"><span></span><div class="brand"><span class="brand-square"></span><span class="brand-name">Daniel R. Halvorsen</span></div></div>
    </div>
  </section>

  <section class="folder folder-closed folder-rear">
    <div class="pocket">
      <div class="pocket-band"></div>
      <div class="pocket-content"><span></span><div class="brand"><span class="brand-square"></span><span class="brand-name">Daniel R. Halvorsen</span></div></div>
    </div>
  </section>

</main>
</body>
</html>
```